BrightMop Tidewater Commercial Cleaning Brochure

We need a tri fold brochure that we can use to market our commercial cleaning services to clients. We are looking for something that will stand out. We don't want to use any faces of people on the brochures, only cleaning tools and supplies. We offer Office Cleaning, Covid Cleaning, Janitorial and Floor Services

Target Market(s)

Small to large businesses

Industry/Entity Type

Commercial Cleaning

Colors
0054AA
0677BA
7BADD7
CADEEF
E8F1F8
0094D4
00A9DD
6FCCEA
C7EBF8
E9F6FB
00AB8E
00BBA5
67D7C9
C6EFE9
E9F9F6
59FF00
82FF00
B8FF75
E3FFCB
F4FFEA

Requirements
Must have
• Stand out design-Eye Catching
Should not have
• faces of ppl the brochure

```html
<!DOCTYPE html>
<html lang="en">
<head>
<meta charset="UTF-8">
<title>BrightMop Tidewater – Commercial Cleaning Tri-fold Brochure</title>
<link href="https://fonts.googleapis.com/css2?family=Open+Sans:ital,wght@0,400;0,600;0,700;0,800;1,400;1,700&display=swap" rel="stylesheet">
<style>
  :root{
    --navy:#0b3486;
    --blue:#0054AA;
    --blue-mid:#0677BA;
    --sky:#0094D4;
    --sky-light:#6FCCEA;
    --green:#82c341;
    --green-deep:#5fa82c;
    --green-bright:#59FF00;
    --ink:#1d2b4a;
    --paper:#ffffff;
    --stage:#e6e8eb;
    --photo-a:#c9d3dc;
    --photo-b:#eef2f6;
  }
  *{box-sizing:border-box;margin:0;padding:0}
  html,body{width:1200px;height:2400px;overflow:hidden}
  body{background:var(--stage);font-family:"Open Sans",Arial,sans-serif;color:var(--ink);position:relative}

  .spread{position:absolute;left:50px;width:1100px;height:850px;display:grid;grid-template-columns:repeat(3,1fr);background:var(--paper);box-shadow:0 14px 40px rgba(20,30,60,.22)}
  .spread--outside{top:300px}
  .spread--inside{top:1250px}
  .panel{position:relative;overflow:hidden;height:850px}
  .wave{position:absolute;left:0;width:100%;display:block}

  .photo{position:absolute;background:linear-gradient(160deg,var(--photo-b),var(--photo-a))}

  .pill{position:absolute;display:inline-block;background:var(--blue);color:#fff;font-weight:700;font-size:15px;letter-spacing:.5px;text-transform:uppercase;padding:6px 22px;border-radius:0 20px 20px 0}
  .body-copy{position:absolute;font-size:13px;line-height:1.6;font-style:italic}

  .brand{font-weight:700;font-size:30px;color:var(--blue);display:flex;align-items:center;gap:10px;white-space:nowrap}
  .brand__dot{width:14px;height:14px;border-radius:50%;background:var(--green)}
  .brand--light{color:#fff}

  .web{font-weight:700;font-size:15px;color:var(--green-bright);display:flex;align-items:center;gap:8px}
  .web__dot{width:12px;height:12px;border-radius:50%;border:2px solid var(--green-bright)}

  /* outside: about panel */
  .about .pill{top:40px;left:0}
  .about .body-copy{top:92px;left:34px;right:28px}
  .about .photo{top:440px;left:0;right:0;height:300px;background:linear-gradient(170deg,#f5f7fa,#b9c5d2 70%,#8fa0b4)}
  .about__band-text{position:absolute;left:34px;bottom:46px;color:#fff;font-weight:700;font-style:italic;font-size:15px;text-transform:uppercase;line-height:1.35}

  /* outside: contact panel */
  .contact{background:var(--green)}
  .contact__photo{position:absolute;top:46px;left:73px;width:220px;height:220px;border-radius:50%;border:6px solid #fff;background:linear-gradient(150deg,#f4f6f8,#aebccb)}
  .contact__badge{position:absolute;top:200px;left:258px;width:78px;height:78px;border-radius:50%;background:var(--navy);border:3px solid #fff;color:#fff;font-weight:800;font-size:11px;text-align:center;display:flex;align-items:center;justify-content:center;line-height:1.2}
  .contact__cta{position:absolute;top:298px;left:0;right:0;text-align:center;color:#fff;font-weight:800;font-size:24px}
  .phone-pill{position:absolute;background:var(--navy);color:#fff;font-weight:700;font-size:19px;border-radius:20px;padding:6px 20px;display:flex;align-items:center;gap:10px}
  .contact .phone-pill{top:340px;left:48px}
  .contact__email{position:absolute;top:392px;left:0;right:0;text-align:center;color:var(--navy);font-weight:700;font-size:15px}
  .contact .body-copy{top:424px;left:36px;right:36px;color:#fff;text-align:center}
  .contact .brand{position:absolute;top:690px;left:0;right:0;justify-content:center}
  .contact .web{position:absolute;top:752px;left:0;right:0;justify-content:center}

  /* outside: cover */
  .cover .brand{position:absolute;top:52px;left:0;right:0;justify-content:center;font-size:34px}
  .cover .photo{top:130px;left:0;right:0;height:440px;background:linear-gradient(180deg,#f7f9fb,#cfd8e1 60%,#9fb0c2)}
  .cover__services{position:absolute;top:610px;left:40px;color:#fff;font-weight:800;font-size:25px;line-height:1.25;text-transform:uppercase;list-style:none}
  .cover .web{position:absolute;bottom:46px;left:40px}

  /* inside: commercial */
  .commercial .photo{top:0;left:0;right:0;height:300px;background:linear-gradient(150deg,#eef1f4,#b7c3cf 70%,#d9c24a 88%,#c73c2d)}
  .commercial .pill{top:348px;left:0}
  .commercial .body-copy{top:392px;left:32px;right:26px}
  .commercial__heading{position:absolute;top:520px;left:32px;right:20px;color:var(--blue);font-weight:800;font-size:14px;line-height:1.25;text-transform:uppercase}
  .commercial__list{position:absolute;top:562px;left:50px;right:20px;font-size:13px;line-height:1.5}

  /* inside: services */
  .services{background:linear-gradient(180deg,var(--blue) 0%,var(--navy) 100%)}
  .services .brand{position:absolute;top:50px;left:0;right:0;justify-content:center}
  .services__title{position:absolute;top:120px;left:0;right:0;text-align:center;color:var(--green);font-weight:800;font-size:24px}
  .services .body-copy{top:162px;left:40px;right:40px;color:#fff;text-align:center}
  .service-grid{position:absolute;top:262px;left:20px;right:20px;display:flex;flex-wrap:wrap;justify-content:center;gap:14px 26px}
  .service{width:92px;text-align:center;color:#fff;font-size:11px}
  .service__icon{width:70px;height:70px;border-radius:50%;background:var(--green);margin:0 auto 6px;border:3px solid #fff}
  .services__photos{position:absolute;top:560px;left:20px;right:20px;display:flex;justify-content:center;gap:8px}
  .services__photos span{width:100px;height:100px;border-radius:50%;border:4px solid var(--green);background:linear-gradient(150deg,#f0d54a,#9fb6cc)}
  .services .web{position:absolute;bottom:44px;left:0;right:0;justify-content:center}

  /* inside: covid */
  .covid .pill{top:40px;left:0}
  .covid .body-copy{left:34px;right:28px}
  .covid__p1{top:90px}
  .covid__p2{top:300px}
  .covid__p3{top:370px}
  .covid__promo{position:absolute;top:460px;left:0;background:var(--green);color:#fff;font-weight:800;font-size:15px;text-align:center;padding:6px 28px;border-radius:0 22px 22px 0;line-height:1.3}
  .covid .phone-pill{top:516px;left:34px}
  .covid .photo{top:620px;left:0;right:0;height:230px;background:linear-gradient(160deg,#e8eef4,#a6b8ca)}
  .web-inline{color:var(--blue);font-weight:700;font-style:normal}
</style>
</head>
<body>

<!-- OUTSIDE SPREAD -->
<section class="spread spread--outside">
  <article class="panel about">
    <span class="pill">About Us</span>
    <p class="body-copy">BrightMop Tidewater is a commercial cleaning business in the local area that offers cleaning, janitorial, flooring, electrostatic disinfecting and fogging services to commercial sites throughout the region.<br><br>We have over 15 years of experience and truly believe in providing affordable, high quality cleaning. We carefully select our staff and equipment to promote long working relationships and trusted service.</p>
    <div class="photo" role="img" aria-label="Bright open office with desks and chairs being sanitized"></div>
    <svg class="wave" style="top:640px;height:210px" viewBox="0 0 366 210" preserveAspectRatio="none" aria-hidden="true">
      <path d="M0 60 Q180 0 366 40 L366 210 L0 210Z" fill="var(--green)"/>
      <path d="M0 76 Q180 20 366 58 L366 210 L0 210Z" fill="var(--navy)"/>
    </svg>
    <p class="about__band-text">Commercial &amp; Industrial<br>Cleaning Service</p>
  </article>

  <article class="panel contact">
    <div class="contact__photo" role="img" aria-label="Mop cleaning a polished office floor"></div>
    <div class="contact__badge">FREE<br>ESTIMATE!</div>
    <h2 class="contact__cta">CALL US FIRST!</h2>
    <div class="phone-pill">
      <svg width="18" height="18" viewBox="0 0 24 24" aria-hidden="true"><path fill="#fff" d="M6.6 10.8a15 15 0 0 0 6.6 6.6l2.2-2.2a1 1 0 0 1 1-.25 11.4 11.4 0 0 0 3.6.57 1 1 0 0 1 1 1V20a1 1 0 0 1-1 1A17 17 0 0 1 3 4a1 1 0 0 1 1-1h3.5a1 1 0 0 1 1 1c0 1.25.2 2.45.57 3.57a1 1 0 0 1-.25 1z"/></svg>
      +1 555-014-2270
    </div>
    <p class="contact__email">info@brightmoptidewater.com</p>
    <p class="body-copy">BrightMop Tidewater offers complete free estimates on all work, so you can be sure you're getting the best service at a fair price. Proudly serving customers in and around Harbor Point.</p>
    <svg class="wave" style="top:620px;height:230px" viewBox="0 0 366 230" preserveAspectRatio="none" aria-hidden="true">
      <path d="M0 30 Q180 -10 366 30 L366 230 L0 230Z" fill="var(--blue)"/>
      <path d="M0 46 Q180 8 366 46 L366 230 L0 230Z" fill="var(--navy)"/>
    </svg>
    <div class="brand brand--light"><span class="brand__dot"></span>BrightMop Tidewater</div>
    <div class="web"><span class="web__dot"></span>www.brightmoptidewater.com</div>
  </article>

  <article class="panel cover">
    <div class="brand"><span class="brand__dot"></span>BrightMop</div>
    <div class="photo" role="img" aria-label="Clean modern office interior with large windows"></div>
    <svg class="wave" style="top:500px;height:350px" viewBox="0 0 366 350" preserveAspectRatio="none" aria-hidden="true">
      <path d="M0 90 Q200 20 366 0 L366 350 L0 350Z" fill="var(--sky)"/>
      <path d="M0 110 Q200 40 366 22 L366 350 L0 350Z" fill="var(--blue)"/>
      <path d="M0 140 Q200 70 366 60 L366 350 L0 350Z" fill="var(--navy)"/>
    </svg>
    <ul class="cover__services">
      <li>Office Cleaning</li>
      <li>Covid Cleaning</li>
      <li>Janitorial</li>
      <li>Floor Services</li>
    </ul>
    <div class="web"><span class="web__dot"></span>www.brightmoptidewater.com</div>
  </article>
</section>

<!-- INSIDE SPREAD -->
<section class="spread spread--inside">
  <article class="panel commercial">
    <div class="photo" role="img" aria-label="Cleaning cart, mop bucket and wet floor sign in an office"></div>
    <svg class="wave" style="top:250px;height:90px" viewBox="0 0 366 90" preserveAspectRatio="none" aria-hidden="true">
      <path d="M0 50 Q180 0 366 40 L366 90 L0 90Z" fill="var(--green)"/>
      <path d="M0 62 Q180 20 366 54 L366 90 L0 90Z" fill="var(--blue)"/>
      <path d="M0 74 Q180 40 366 68 L366 90 L0 90Z" fill="#fff"/>
    </svg>
    <span class="pill">Commercial Cleaning</span>
    <p class="body-copy">Experience into working with a diverse group of staff. Maintenance of buildings and facilities. Oversee night shift custodial staff, oversee day all cleaning and janitorial duties per scope of services.</p>
    <h3 class="commercial__heading">Provide elite cleaning services<br>to your location!</h3>
    <ul class="commercial__list">
      <li>Carpet Cleaning Shampoo or extraction</li>
      <li>Detail Carpet Vacuuming</li>
      <li>Floor Care Stripping and Refinishing floor</li>
      <li>Empty trash and recycles daily</li>
      <li>Night Janitorial cleaning</li>
      <li>Maintain Restrooms cleaning</li>
      <li>Polish Floors, Buff floors, Scrub Maintenance</li>
      <li>High low dusting</li>
      <li>Window Cleaning Services</li>
      <li>Exterior Leaf blower services</li>
      <li>Pressure Washer services</li>
    </ul>
  </article>

  <article class="panel services">
    <div class="brand brand--light"><span class="brand__dot"></span>BrightMop Tidewater</div>
    <h2 class="services__title">OUR SERVICES</h2>
    <p class="body-copy">Whether you require a one-time or recurring cleaning for your house or apartment, we're available to personalize your service based on your needs.</p>
    <div class="service-grid">
      <div class="service"><div class="service__icon" role="img" aria-label="Office cleaning icon"></div>Office Cleaning</div>
      <div class="service"><div class="service__icon" role="img" aria-label="Floor care icon"></div>Floor Care</div>
      <div class="service"><div class="service__icon" role="img" aria-label="Janitorial services icon"></div>Janitorial Services</div>
      <div class="service"><div class="service__icon" role="img" aria-label="Covid cleaning icon"></div>Covid Cleaning</div>
      <div class="service"><div class="service__icon" role="img" aria-label="Sanitation supplies icon"></div>Sanitation Supplies</div>
    </div>
    <div class="services__photos">
      <span role="img" aria-label="Wet floor warning sign"></span>
      <span role="img" aria-label="Gloved hand with cleaning supplies"></span>
      <span role="img" aria-label="Disinfecting spray on an office desk"></span>
    </div>
    <div class="web"><span class="web__dot"></span>www.brightmoptidewater.com</div>
  </article>

  <article class="panel covid">
    <span class="pill">Covid Cleaning</span>
    <p class="body-copy covid__p1">We will be offering a service where we go into facilities like residential, office, child care, medical, dental, restaurant, veterinarian, gyms, hotels, automotive, fleets and professional spaces with sanitizing equipment and disinfect their facilities for a fee.</p>
    <p class="body-copy covid__p2">Our products kills a wide range of viruses and pathogens including Covid-19.</p>
    <p class="body-copy covid__p3">We follow all safety procedures and only use EPA approved products. Visit <span class="web-inline">www.brightmoptidewater.com</span> for more.</p>
    <div class="covid__promo">COVID CLEANING SERVICE<br>FREE ESTIMATES</div>
    <div class="phone-pill">
      <svg width="18" height="18" viewBox="0 0 24 24" aria-hidden="true"><path fill="#fff" d="M6.6 10.8a15 15 0 0 0 6.6 6.6l2.2-2.2a1 1 0 0 1 1-.25 11.4 11.4 0 0 0 3.6.57 1 1 0 0 1 1 1V20a1 1 0 0 1-1 1A17 17 0 0 1 3 4a1 1 0 0 1 1-1h3.5a1 1 0 0 1 1 1c0 1.25.2 2.45.57 3.57a1 1 0 0 1-.25 1z"/></svg>
      +1 555-014-2270
    </div>
    <div class="photo" role="img" aria-label="Disinfection fogging of an office workspace"></div>
    <svg class="wave" style="top:600px;height:70px" viewBox="0 0 366 70" preserveAspectRatio="none" aria-hidden="true">
      <path d="M0 0 L366 0 L366 30 Q180 70 0 20Z" fill="#fff"/>
      <path d="M0 20 Q180 70 366 30 L366 40 Q180 80 0 32Z" fill="var(--green)"/>
    </svg>
  </article>
</section>

</body>
</html>
```